New business card design needed for Diesel Fitting (Mechanical) Company

We need a new business card for our company called "Gumtree Engine Works" that showcases our logo and business details.
Target Market(s)
Owners of all makes and models of vehicles, trucks, plant and machinery.
Industry/Entity Type
Mechanical
Contact Information for Business Card
The business card details need to include the following: Owners/Directors: Doug & Marisol Brent-Coyle ABN: 41 917 302 846 Address: 317 Wattlebrook Street CHARTERS TOWERS QLD 4820 Postal Address: PO Box 5791 CHARTERS TOWERS QLD 4820 Website: www.gewservice.com.au Phone: 4712 9083 Mobile: 0438 175 906 Emails: sales@gewservice.com.au; admin@gewservice.com.au; accounts@gewservice.com.au; parts@gewservice.com.au; office@gewservice.com.au, reception@gewservice.com.au
Look and feel

```html
<!DOCTYPE html>
<html lang="en">
<head>
<meta charset="utf-8">
<title>Gumtree Engine Works – Business Card</title>
<link href="https://fonts.googleapis.com/css2?family=Open+Sans:wght@400;600;700&display=swap" rel="stylesheet">
<style>
  :root {
    --backdrop: #2a2a2a;
    --card: #161616;
    --orange: #f26b21;
    --yellow: #f7b21a;
    --grey: #9a9a9a;
    --white: #f2f2f2;
  }
  * { margin: 0; padding: 0; box-sizing: border-box; }
  html, body {
    width: 1200px; height: 900px; overflow: hidden;
    background: var(--backdrop);
    font-family: "Open Sans", Arial, sans-serif;
  }
  .card {
    position: absolute; left: 150px; top: 180px;
    width: 900px; height: 540px;
    background: var(--card);
    color: var(--white);
    box-shadow: 0 20px 50px rgba(0,0,0,.55);
  }
  .brand {
    position: absolute; left: 70px; top: 90px;
    display: flex; align-items: center; gap: 16px;
  }
  .brand-dot {
    width: 46px; height: 46px; border-radius: 50%;
    background: var(--orange);
    flex: none;
  }
  .brand-name {
    font-size: 38px; font-weight: 700; line-height: 1.05;
    color: var(--orange); width: 300px;
  }
  .divider {
    position: absolute; left: 480px; top: 140px;
    width: 2px; height: 230px; background: var(--orange);
  }
  .contact {
    position: absolute; left: 510px; top: 140px;
    font-size: 17px; line-height: 1.45;
  }
  .contact-name {
    font-size: 24px; font-weight: 700; color: var(--orange); line-height: 1.2;
  }
  .contact-role { color: var(--grey); font-size: 16px; margin-bottom: 6px; }
  .label { color: var(--yellow); }
  .contact-line { display: flex; align-items: center; gap: 10px; }
  .contact-line svg { width: 16px; height: 16px; flex: none; }
  .emails {
    position: absolute; left: 60px; bottom: 60px;
    font-size: 16px; line-height: 1.7;
  }
  .emails .sep { color: var(--yellow); margin: 0 10px; }
</style>
</head>
<body>
  <div class="card">
    <div class="brand">
      <span class="brand-dot"></span>
      <span class="brand-name">Gumtree Engine Works</span>
    </div>

    <div class="divider"></div>

    <div class="contact">
      <div class="contact-name">Doug &amp; Marisol Brent-Coyle</div>
      <div class="contact-role">Owners/Directors</div>
      <div><span class="label">Address:</span> 317 Wattlebrook Street</div>
      <div>Kallaroo Flats, QLD 4871</div>
      <div><span class="label">Postal Address:</span> PO Box 5791</div>
      <div>Kallaroo Flats, QLD 4871</div>
      <div class="contact-line">
        <svg viewBox="0 0 16 16"><path fill="var(--yellow)" d="M3 1l3 3-1.5 2a9 9 0 005.5 5.5L12 10l3 3-2 2C7 15 1 9 1 3z"/></svg>
        07 4712 9083
      </div>
      <div class="contact-line">
        <svg viewBox="0 0 16 16"><rect x="4" y="1" width="8" height="14" rx="1.5" fill="none" stroke="var(--yellow)" stroke-width="1.6"/><circle cx="8" cy="12.5" r="1" fill="var(--yellow)"/></svg>
        0438 175 906
      </div>
      <div class="contact-line">
        <svg viewBox="0 0 16 16"><circle cx="8" cy="8" r="6.5" fill="none" stroke="var(--yellow)" stroke-width="1.5"/><path d="M1.5 8h13M8 1.5c-3 3.5-3 9.5 0 13M8 1.5c3 3.5 3 9.5 0 13" fill="none" stroke="var(--yellow)" stroke-width="1.2"/></svg>
        www.gewservice.com.au
      </div>
    </div>

    <div class="emails">
      <div>sales@gewservice.com.au<span class="sep">•</span>admin@gewservice.com.au<span class="sep">•</span>accounts@gewservice.com.au</div>
      <div>parts@gewservice.com.au<span class="sep">•</span>office@gewservice.com.au<span class="sep">•</span>reception@gewservice.com.au</div>
    </div>
  </div>
</body>
</html>
```